Resume for higher management position in a mechanical/consultant industries application*

I would like to use this resume for getting a higher position interview possibilities. My skills are multi-cultural negotiation, mechanical industry sales, outsourcing to Asia, ability to manage the agent/reseller system, well team player. multi-language Chinese/English/German specialized. Please make the design, professional, comfortable to read atmosphere.

Target Market(s)

management position, sales related

Font styles to use
Serif
Sans Serif

```html
<!DOCTYPE html>
<html lang="en">
<head>
<meta charset="utf-8">
<title>Wei-Lin Tsai – Resume</title>
<link href="https://fonts.googleapis.com/css2?family=Arimo:wght@400;500;700&display=swap" rel="stylesheet">
<style>
:root{
  --backdrop:#8a8a8a;
  --paper:#ffffff;
  --sky:#b3e5f9;
  --ink:#111111;
  --rule:#8fc9df;
}
*{margin:0;padding:0;box-sizing:border-box}
html,body{width:1200px;height:1200px;overflow:hidden;background:var(--backdrop)}
body{font-family:"Arimo",Arial,sans-serif;color:var(--ink);position:relative}
.resume{position:absolute;left:373.6px;top:282.4px;width:566px;height:793px;background:var(--paper);transform:scale(.8);transform-origin:0 0}
.resume *{position:absolute}
.sidebar{left:0;top:0;width:235px;height:793px;background:var(--sky)}
.photo-slot{left:49px;top:30px;width:132px;height:132px;border-radius:50%;background:var(--paper)}
.text{font-size:9.6px;line-height:12px}
.strong{font-weight:700}
.side-text{left:17px;width:205px}
.divider{left:14px;top:414px;width:208px;height:1px;background:var(--rule)}
.side-heading{left:15px;top:619px;font-size:12.5px;font-weight:500}
.name{left:256px;top:17px;font-size:31px;font-weight:700;letter-spacing:.3px;white-space:nowrap}
.role{left:259px;top:52px;font-size:17.5px;white-space:nowrap}
.band{left:235px;height:28px;background:var(--sky)}
.band-title{font-size:18.5px;font-weight:700;top:4px;white-space:nowrap}
.entry{width:280px}
.date{font-size:9.6px;line-height:12px;white-space:nowrap;text-align:right}
.tick{left:248px;width:8px;height:8px}
</style>
</head>
<body>
<main class="resume">
  <aside class="sidebar">
    <div class="photo-slot" role="img" aria-label="Portrait photo placeholder"></div>
    <p class="text strong side-text" style="top:198px">Mandarin Chinese/ German/ English speaker, real machining experiences, OEM skills, trade skill, global sourcing</p>
    <p class="text side-text" style="top:246px">Currently, I am a “Sales manager Asia” of a top German rotary table company. I am in charge of four countries Japan, China, South Korea and Taiwan with 3 agents, more than 20 salemen team.</p>
    <p class="text side-text" style="top:318px">As a director of manufacuturing, I have more than 5 years professional experiences in manufacturing metal components by different CNC-machines. I am capable of coding CNC G,M-code, designing the working path of different parts and managing the whole process.</p>
    <div class="divider"></div>
    <p class="text side-text" style="top:424px">I have well-understanding of mechanical outsourcing ecosystem in Taiwan. With deep knowledge of outsourcing metal components to different suppliers in Taiwan.</p>
    <p class="text side-text" style="top:484px">Familiar with coordinating with different industrial processes in order to build the final products. (Black oxidizing, Different anodizing, Chemical polishing, Manganese phosphate coating, Heat treatment, and Different grinding methods) Especially love to build prototype in order to get a high profitable potential products. (from zero to one)</p>
    <h3 class="side-heading">Personal Information</h3>
    <p class="text side-text" style="left:16px;top:642px">Name: Wei-Lin Tsai<br>Date &amp; Place of birth: xxxxxxx<br>Nationality: Taiwanese<br>Address: xxxxxxxx, Germany<br>Mobile: +xxxxxx<br>Email: xxxxxx@mailbox.com</p>
  </aside>

  <h1 class="name">WEI-LIN TSAI</h1>
  <p class="role">Sales Manager Asia</p>

  <div class="band" style="top:85px;width:209px"></div>
  <h2 class="band-title" style="left:263px;top:89px">WORK EXPERIENCE</h2>

  <p class="text strong" style="left:264px;top:127px">Sales Manager Asiaxxxxxxxxxx</p>
  <p class="date" style="left:440px;top:127px;width:99px">2018-present</p>
  <p class="text entry" style="left:264px;top:147px;width:270px">Currently, leading 3 major dealers in Taiwan, Mainland China, South Korea and Japan with more than 20 salesmen team.</p>
  <p class="text entry" style="left:264px;top:195px;width:275px">Haldorf provides rotary tables, trunnions and 2 axis rotary tilt units shall have the best possible technical characteristics in the smallest possible space, is the principle model for our dividing heads -engineering -manufacturing -and assembly.</p>

  <p class="text strong" style="left:265px;top:259px">Director of Manufacturing,<br>Brennstein Precision Machinery Company</p>
  <p class="date" style="left:440px;top:271px;width:98px">2012-2017</p>
  <p class="text entry" style="left:266px;top:293px;width:270px">Using CNC turn/mill machine to manufacture any mechanical components as customers want. Also providing great total solutions for our clients.</p>

  <p class="text strong" style="left:265px;top:342px">Marketing Analyst, Fresh Path Import<br>Mannheim Germany,</p>
  <p class="date" style="left:420px;top:354px;width:116px">2012 Apr- 2012 Nov</p>
  <p class="text entry" style="left:266px;top:374px;width:280px">Help Fresh Path Import to build their sales/marketing strategy for the new launched product “Slickguard” in central Europe.</p>

  <p class="text strong" style="left:267px;top:411px">External consultant, Corvalto<br>Group Bergamo Italty,</p>
  <p class="date" style="left:430px;top:424px;width:112px">2011 Oct-2012 Mar</p>
  <p class="text entry" style="left:268px;top:447px;width:280px">To improve the Nexa solution(ERP system) of Corvalto with re-organized procurement process and new standardized KPIs.</p>

  <div class="band" style="top:494px;width:147px"></div>
  <h2 class="band-title" style="left:266px;top:498px">EDUCATION</h2>

  <p class="text strong" style="left:263px;top:539px">MBA, Politecnico Lombardo Italy</p>
  <p class="text" style="left:470px;top:539px">2011-2012</p>
  <p class="text strong" style="left:263px;top:563px">Bachelor of Chemical engineering,<br>Tai-Ho Christian University</p>
  <p class="text" style="left:470px;top:575px">2005-2009</p>

  <div class="band" style="top:612px;width:241px"></div>
  <h2 class="band-title" style="left:264px;top:616px">SKILLS and EXPERTISE</h2>

  <svg class="tick" style="top:656px" viewBox="0 0 8 8"><path d="M1 4.2 3 6.2 7 1.8" fill="none" stroke="var(--ink)" stroke-width="1.3"/></svg>
  <p class="text strong" style="left:264px;top:654px">MBA degree from LBS, Politecnico Lombardo.</p>
  <svg class="tick" style="top:680px" viewBox="0 0 8 8"><path d="M1 4.2 3 6.2 7 1.8" fill="none" stroke="var(--ink)" stroke-width="1.3"/></svg>
  <p class="text strong" style="left:264px;top:678px">Specialties: Great experiences in handling business<br>with Chinese-cultural business firms.</p>
  <svg class="tick" style="top:716px" viewBox="0 0 8 8"><path d="M1 4.2 3 6.2 7 1.8" fill="none" stroke="var(--ink)" stroke-width="1.3"/></svg>
  <p class="text strong" style="left:264px;top:714px">Multi-national corporation skills<br>( especially in Chinese-speaking market)</p>
  <svg class="tick" style="top:752px" viewBox="0 0 8 8"><path d="M1 4.2 3 6.2 7 1.8" fill="none" stroke="var(--ink)" stroke-width="1.3"/></svg>
  <p class="text strong" style="left:264px;top:750px">Multi-language skill: native Chinese speaker/<br>advanced English/ advanced German</p>
</main>
</body>
</html>
```